Stationery Design Project for a consulting/educational company

We need a stationery design for a consulting / educational company called "VORT d.o.o.". We are an official partner (yet stand-alone company) of the MELQ Institute, Germany (www.melq-example.de) that covers practically all themes regarding production optimisation, efectiveness, productivity (time studies, workplace organisation,...) We need the design for:

- a CERTIFICATE for seminar participates
- business cards
- letterhead

We are changing our webpage to their design, so we need to change the stationaries as well. I included 2 current logos, one with current color scheme (not important) and the other black/white with a frame. I also included the MELQ original certificate. Only the font + name"VORT" is important, the rest is up to you
Updates

Designs look good, but perhaps a gray & green combo would look nicer? Like on www.melq-example.de? And without the frames?

Target Market(s)

Larger production companies top and middle management

Industry/Entity Type

Business

Requirements
Must have
• - the stationaries (all of them) should, besides the company name "VORT", also include the logo MELQ (in its color), like on their webpage www.melq-example.de
Nice to have
• - certificate could use 5th color (e.g. silver) to make an impression
- similar color scheme to www.melq-example.de

```html
<!DOCTYPE html>
<html lang="en">
<head>
<meta charset="utf-8">
<title>VORT d.o.o. – Business Card</title>
<link href="https://fonts.googleapis.com/css2?family=Open+Sans:ital,wght@0,400;0,700;1,700&display=swap" rel="stylesheet">
<style>
  :root {
    --page-bg: #2b3032;
    --card-bg: #ffffff;
    --accent: #02a8ab;
    --ink: #3a3a3a;
    --mark: #151515;
  }
  * { margin: 0; padding: 0; box-sizing: border-box; }
  html, body { width: 987px; height: 1200px; overflow: hidden; }
  body {
    background: var(--page-bg);
    font-family: "Open Sans", Arial, sans-serif;
    color: var(--ink);
    position: relative;
  }
  .card {
    position: absolute;
    width: 790px;
    height: 452px;
    background: var(--card-bg);
    border-radius: 30px;
    overflow: hidden;
    box-shadow: 0 6px 14px rgba(0,0,0,0.45);
  }
  .card--front { left: 95px; top: 105px; }
  .card--back  { left: 93px; top: 645px; }

  .card__swoosh { position: absolute; inset: 0; width: 790px; height: 452px; }

  .brand-name {
    position: absolute;
    font-weight: 700;
    color: var(--mark);
    letter-spacing: 2px;
    line-height: 1;
    text-align: center;
  }
  .card--front .brand-name { left: 130px; top: 68px; width: 390px; font-size: 108px; }
  .card--back  .brand-name { left: 0; top: 95px; width: 790px; font-size: 160px; }

  .partner {
    position: absolute;
    left: 238px; top: 190px;
    display: flex; align-items: center; gap: 12px;
  }
  .partner__square { width: 34px; height: 34px; background: var(--accent); }
  .partner__name { font-size: 40px; font-weight: 700; color: var(--accent); line-height: 1; letter-spacing: 1px; }

  .contact {
    position: absolute;
    left: 100px; top: 284px; width: 450px;
    text-align: center;
  }
  .contact__name { font-size: 24px; font-weight: 700; line-height: 1.2; }
  .contact__role { font-size: 19px; font-weight: 400; }
  .contact__line { font-size: 19px; line-height: 1.2; margin-top: 13px; }
  .contact__line + .contact__line { margin-top: 12px; }
  .contact__label { font-weight: 700; font-style: italic; }

  .card__web {
    position: absolute;
    left: 0; top: 380px; width: 790px;
    text-align: center;
    font-size: 32px;
  }
</style>
</head>
<body>
  <section class="card card--front">
    <svg class="card__swoosh" viewBox="0 0 790 452" aria-hidden="true">
      <path d="M545 0 L790 0 L790 452 L665 452 C760 330 760 140 545 0 Z" fill="var(--accent)"/>
      <path d="M622 0 L668 0 C760 90 770 250 722 390 C742 240 720 110 622 0 Z" fill="var(--card-bg)"/>
    </svg>
    <div class="brand-name">VORT</div>
    <div class="partner">
      <span class="partner__square"></span>
      <span class="partner__name">MELQ</span>
    </div>
    <div class="contact">
      <p class="contact__name">Your Name - <span class="contact__role">Designation</span></p>
      <p class="contact__line"><span class="contact__label">t</span> : 0123-456-789 &nbsp;|&nbsp; <span class="contact__label">f</span> : 0123-456-789</p>
      <p class="contact__line"><span class="contact__label">e</span> : info@website.de &nbsp;|&nbsp; <span class="contact__label">w</span> : www.website.com</p>
      <p class="contact__line">Street Name, City Name, State, City Zip Code.</p>
    </div>
  </section>

  <section class="card card--back">
    <div class="brand-name">VORT</div>
    <p class="card__web">www.website.com</p>
  </section>
</body>
</html>
```